Pregnancy and Fertility Information Website

Hello Designers,
I need a website which provide tips and information about healthy and happy pregnancy. My website name is Lorvin medical.

The website should provide all the information needed throughout pregnancy and beyond ranging from pregnancy tracking tools and articles about common pregnancy concerns and what to expect during pregnancy,etc.
The details about first trimester, second trimester and third trimester should be highlighted in the website.

Top Navigation
Home, Fertility, Pregnancy basics, Articles, Tips and News

I'm looking for a simple and clean design which involves captivating images and colors but it shouldn't be crowded. The design must be professional and modern. An easy to navigate layout is a must.

Green, violet, blue and light yellow colors are my favorites but i'm open to other options.

Any questions. Kindly ask

Industry/Entity Type

Medical

```html
<!DOCTYPE html>
<html lang="en">
<head>
<meta charset="utf-8">
<title>Lorvin Medical – Pregnancy &amp; Fertility</title>
<link href="https://fonts.googleapis.com/css2?family=Dosis:wght@500;600;700&family=PT+Serif&display=swap" rel="stylesheet">
<style>
:root{
  --board:#4a3834;
  --board-label:#9d918c;
  --green:#9cbf1e;
  --green-dark:#86a814;
  --brown:#5b4a2a;
  --ink:#2b2b2b;
  --muted:#6a6a6a;
  --yellow:#fdfee2;
  --violet:#8a4a9c;
  --violet-soft:#b07bc0;
  --pink:#e04fa4;
  --orange:#ef6a1f;
  --footer:#2c2624;
  --footer-text:#bdb6b2;
  --white:#ffffff;
}
*{box-sizing:border-box;margin:0;padding:0}
html,body{width:1200px;height:3000px;overflow:hidden;background:var(--board)}
body{position:relative;font-family:"PT Serif",Georgia,serif;color:var(--ink)}
.board-label{position:absolute;top:48px;left:0;width:1200px;text-align:center;font-family:"Dosis",sans-serif;font-weight:700;font-size:36px;letter-spacing:1px;color:var(--board-label)}
.site{position:absolute;left:36px;top:144px;width:1110px;height:2636px;background:var(--white);overflow:hidden}
.abs{position:absolute}
.heading{font-family:"Dosis",sans-serif;font-weight:700;text-transform:uppercase}
.small{font-size:9px;line-height:12px;color:var(--muted)}
/* header */
.topbar-phone{left:254px;top:6px;font-size:9px;color:var(--muted);display:flex;align-items:center;gap:8px}
.phone-dot{width:16px;height:16px;border-radius:50%;background:var(--green)}
.topbar-address{left:706px;top:8px;font-size:9px;color:var(--muted)}
.brand{left:480px;top:10px;display:flex;align-items:center;gap:8px;font-family:"Dosis",sans-serif;font-weight:700;font-size:15px;color:var(--green)}
.brand-dot{width:22px;height:22px;border-radius:50%;background:var(--orange)}
.nav{top:42px;font-family:"Dosis",sans-serif;font-weight:700;font-size:10px;color:var(--ink);text-transform:uppercase}
.nav.active{color:var(--green)}
/* hero */
.hero{left:0;top:60px;width:1110px;height:490px;background:linear-gradient(90deg,#e9f6dc 0%,#eef7e4 40%,#f2f0ea 100%)}
.hero-photo{left:300px;top:0;width:770px;height:490px;background:linear-gradient(120deg,#e9f1e0 0%,#e9c8a8 45%,#d9a47f 75%,#c58b6a 100%)}
.hero-curve{left:0;top:470px}
.hero-title{left:184px;top:164px;font-family:"Dosis",sans-serif;font-weight:700;font-size:40px;line-height:42px;color:var(--brown);text-align:center;width:270px}
.hero-sub{left:150px;top:286px;font-family:"Dosis",sans-serif;font-weight:600;font-size:17px;color:var(--green-dark)}
.hero-brand{left:228px;top:316px;display:flex;align-items:center;gap:10px;font-family:"Dosis",sans-serif;font-weight:700;font-size:19px;color:var(--green-dark);text-transform:uppercase}
.hero-brand .brand-dot{width:34px;height:34px}
/* welcome */
.welcome-title{left:254px;top:600px;font-size:17px;color:var(--ink)}
.welcome-title span{color:var(--green)}
.welcome-text{left:254px;top:648px;width:300px}
.welcome-photo{left:254px;top:706px;width:244px;height:140px;background:linear-gradient(135deg,#f3d9c8,#dca88d 60%,#c98f78)}
.guide-line{left:618px;top:550px;width:1px;height:340px;background:#e4e4e4}
.guide-item{left:590px;display:flex;gap:22px;width:400px}
.guide-thumb{width:54px;height:54px;border-radius:50%;flex:none;border:3px solid #fff;box-shadow:0 0 0 1px #e2e2e2;background:linear-gradient(135deg,#f2d8c6,#cf9a80)}
.guide-item h4{font-family:"Dosis",sans-serif;font-weight:700;font-size:11px;text-transform:uppercase;margin:2px 0 6px}
/* pregnancy guide band */
.band{left:0;top:896px;width:1110px;height:424px;background:var(--yellow)}
.section-title{left:0;width:1110px;text-align:center;font-size:22px;color:var(--green)}
.section-sub{left:0;width:1110px;text-align:center;font-size:9px;color:var(--muted)}
.rule{left:540px;width:30px;height:2px;background:var(--green)}
.topic{width:230px}
.topic h4{font-family:"Dosis",sans-serif;font-weight:700;font-size:11px;text-transform:uppercase;margin-bottom:4px}
.topic.left{text-align:right}
.topic-icon{width:44px;height:44px;border-radius:50%;background:var(--green);display:flex;align-items:center;justify-content:center}
.topic-icon i{width:14px;height:14px;border-radius:50%;background:var(--white)}
.hub{left:462px;top:1058px;width:192px;height:192px;border-radius:50%;border:6px solid var(--white);box-shadow:0 0 0 1px #dde6b5;background:linear-gradient(180deg,#f1e6de 0%,#d9b9a7 55%,#7d6a96 56%,#6e5a8a 100%);overflow:hidden}
.hub-label{left:462px;top:1166px;width:192px;text-align:center;font-family:"Dosis",sans-serif;font-weight:700;font-size:19px;line-height:22px;color:var(--white)}
/* stages */
.stages-bg{left:0;top:1320px;width:1110px;height:540px;background:linear-gradient(180deg,#fff 0%,#f8f1f8 50%,#fff 100%)}
.stage{width:240px;text-align:right}
.stage h4{font-family:"Dosis",sans-serif;font-weight:700;font-size:11px;text-transform:uppercase;margin-bottom:4px}
.stage-icon{width:44px;height:44px;border-radius:50%;background:var(--violet)}
.stages-art{left:566px;top:1498px;width:300px;height:240px;background:linear-gradient(90deg,#efe2f2,#d9b6e0 50%,#efe2f2)}
.ribbon{left:636px;top:1474px;width:130px;height:18px;background:var(--pink);color:var(--white);font-size:9px;text-align:center;line-height:18px;font-family:"Dosis",sans-serif;font-weight:700;text-transform:uppercase}
.timeline{left:566px;top:1744px;width:300px;height:16px;display:flex}
.timeline span{flex:1;font-size:9px;line-height:16px;color:var(--white);text-align:center;font-family:"Dosis",sans-serif;font-weight:700}
/* posts */
.post{width:186px}
.post-photo{height:124px;background:linear-gradient(135deg,#eac9b5,#c78e72)}
.post-date{width:34px;height:34px;border-radius:50%;background:var(--green);color:var(--white);font-size:7px;line-height:9px;text-align:center;padding-top:8px;margin:-17px 0 0 14px;position:relative;border:2px solid #fff;font-family:"Dosis",sans-serif;font-weight:700}
.post h4{font-family:"Dosis",sans-serif;font-weight:700;font-size:11px;line-height:13px;text-transform:uppercase;margin:10px 0 6px}
.read-more{display:inline-block;margin-top:12px;border:1px solid #d2d2d2;border-radius:12px;padding:4px 16px;font-family:"Dosis",sans-serif;font-weight:700;font-size:8px;text-transform:uppercase}
/* footer */
.footer{left:0;top:2292px;width:1110px;height:208px;background:linear-gradient(90deg,#2a2422,#3a2f2b 70%,#4b3a35)}
.foot-col h5{font-family:"Dosis",sans-serif;font-weight:700;font-size:10px;color:var(--white);text-transform:uppercase;margin-bottom:14px}
.foot-col li{list-style:none;font-size:9px;color:var(--footer-text);margin-bottom:7px;display:flex;align-items:center;gap:8px}
.foot-col li b{width:7px;height:7px;border-radius:50%;background:var(--footer-text);display:inline-block}
.foot-photo{left:714px;top:2342px;width:140px;height:120px;background:linear-gradient(135deg,#e9c6b6,#c49080);border:3px solid #fff}
.subscribe{left:0;top:2500px;width:1110px;height:86px;background:var(--green)}
.subscribe h5{font-family:"Dosis",sans-serif;font-weight:700;font-size:12px;color:var(--white);text-transform:uppercase}
.sub-field{left:440px;top:2532px;width:212px;height:22px;border:1px solid #e5f1b3;border-radius:12px}
.sub-go{left:630px;top:2536px;width:14px;height:14px;border-radius:50%;background:#e5f1b3}
.social{top:2532px;width:22px;height:22px;border-radius:50%;border:1px solid #e5f1b3}
.copyright{left:0;top:2586px;width:1110px;height:50px;background:var(--footer);font-size:8px;color:#8a817d;padding:16px 254px}
</style>
</head>
<body>
<div class="board-label">DESIGN IDEA-02</div>

<main class="site">
  <!-- header -->
  <div class="abs topbar-phone"><span class="phone-dot"></span>(02) 55 010 240</div>
  <div class="abs brand"><span class="brand-dot"></span>LORVIN MEDICAL</div>
  <div class="abs topbar-address"><b>Address :</b> 14 Alder Lane 4410 2090</div>
  <nav>
    <a class="abs nav active" style="left:254px">Home</a>
    <a class="abs nav" style="left:308px">Fertility</a>
    <a class="abs nav" style="left:376px">Pregnancy Basics</a>
    <a class="abs nav" style="left:658px">Articles</a>
    <a class="abs nav" style="left:724px">Tips &amp; News</a>
    <a class="abs nav" style="left:804px">Contact Us</a>
  </nav>

  <!-- hero -->
  <section class="abs hero">
    <div class="abs hero-photo" role="img" aria-label="Photo of a mother holding her newborn baby close"></div>
    <svg class="abs hero-curve" width="1110" height="30" viewBox="0 0 1110 30"><path d="M0 30 Q555 -10 1110 30 Z" fill="#fff"/></svg>
  </section>
  <h1 class="abs hero-title">Feel Safe With Mom's Care</h1>
  <p class="abs hero-sub">Best resource needed throughout pregnancy</p>
  <div class="abs hero-brand"><span class="brand-dot"></span>Lorvin Medical</div>

  <!-- welcome -->
  <h2 class="abs heading welcome-title">Welcome to <span>"Lorvin Medical"</span></h2>
  <p class="abs small welcome-text">Lorvin Medical is an online resource committed to providing information needed throughout pregnancy and beyond ranging from pregnancy tracking tools and articles about common pregnancy concerns and what to expect during pregnancy.</p>
  <div class="abs welcome-photo" role="img" aria-label="Photo of a newborn baby lying on a blanket"></div>

  <div class="abs guide-line"></div>
  <div class="abs guide-item" style="top:598px"><div class="guide-thumb" role="img" aria-label="Photo of a pregnant woman"></div><div><h4>Pregnancy Guide</h4><p class="small">Complete Guide To Pregnancy Lorem Ipsum<br>is simply dummy text of the printing and<br>typesetting industry</p></div></div>
  <div class="abs guide-item" style="top:692px"><div class="guide-thumb" role="img" aria-label="Photo of a parent caring for a baby"></div><div><h4>Baby Care Guide</h4><p class="small">Complete Guide To Baby Care Lorem Ipsum<br>is simply dummy text of the printing and<br>typesetting industry</p></div></div>
  <div class="abs guide-item" style="top:784px"><div class="guide-thumb" role="img" aria-label="Photo of healthy food for nutrition"></div><div><h4>Nutrition Guide</h4><p class="small">Complete Guide To Nutrition Lorem Ipsum<br>is simply dummy text of the printing and<br>typesetting industry</p></div></div>

  <!-- pregnancy guide -->
  <section class="abs band"></section>
  <h2 class="abs heading section-title" style="top:940px">Pregnancy Guide</h2>
  <p class="abs section-sub" style="top:970px">This provides all the details related to the pregnancy</p>
  <div class="abs rule" style="top:990px"></div>

  <div class="abs topic left" style="left:236px;top:1048px"><h4>Getting Pregnant</h4><p class="small">Lorem Ipsum is simply dummy text of the<br>printing and typesetting industry</p></div>
  <div class="abs topic-icon" style="left:478px;top:1046px"><i></i></div>
  <div class="abs topic left" style="left:204px;top:1140px"><h4>Your First Scan</h4><p class="small">Lorem Ipsum is simply dummy text of the<br>printing and typesetting industry</p></div>
  <div class="abs topic-icon" style="left:446px;top:1140px"><i></i></div>
  <div class="abs topic left" style="left:236px;top:1238px"><h4>Pregnant</h4><p class="small">Lorem Ipsum is simply dummy text of the<br>printing and typesetting industry</p></div>
  <div class="abs topic-icon" style="left:478px;top:1236px"><i></i></div>

  <div class="abs hub" role="img" aria-label="Photo of an expectant mother reading a guide"></div>
  <div class="abs hub-label">PREGNANCY<br>GUIDE</div>

  <div class="abs topic-icon" style="left:594px;top:1046px"><i></i></div>
  <div class="abs topic" style="left:650px;top:1048px"><h4>Baby Birth</h4><p class="small">Lorem Ipsum is simply dummy text of the<br>printing and typesetting industry</p></div>
  <div class="abs topic-icon" style="left:626px;top:1140px"><i></i></div>
  <div class="abs topic" style="left:682px;top:1140px"><h4>Feeding Baby</h4><p class="small">Lorem Ipsum is simply dummy text of the<br>printing and typesetting industry</p></div>
  <div class="abs topic-icon" style="left:594px;top:1236px"><i></i></div>
  <div class="abs topic" style="left:650px;top:1238px"><h4>Baby Care</h4><p class="small">Lorem Ipsum is simply dummy text of the<br>printing and typesetting industry</p></div>

  <!-- pregnancy stages -->
  <section class="abs stages-bg"></section>
  <h2 class="abs heading section-title" style="top:1364px">Pregnancy Stages</h2>
  <p class="abs section-sub" style="top:1394px">This section provides information about Trimesters</p>
  <div class="abs rule" style="top:1414px"></div>

  <div class="abs stage" style="left:226px;top:1472px"><h4>I Trimester</h4><p class="small">This gives information about the 1st trimester.<br>Lorem ipsum dolor sit amet, consectetur<br>adipiscing elit, sed do eiusmod tempor</p></div>
  <div class="abs stage-icon" style="left:476px;top:1474px"></div>
  <div class="abs stage" style="left:226px;top:1558px"><h4>II Trimester</h4><p class="small">This gives information about the 2nd trimester.<br>Lorem Ipsum has been the industry's standard<br>dummy text ever since the 1500s</p></div>
  <div class="abs stage-icon" style="left:476px;top:1560px"></div>
  <div class="abs stage" style="left:226px;top:1648px"><h4>III Trimester</h4><p class="small">This gives information about the 3rd trimester.<br>Lorem Ipsum is simply dummy text of the<br>printing and typesetting industry</p></div>
  <div class="abs stage-icon" style="left:476px;top:1650px"></div>
  <div class="abs stage" style="left:226px;top:1730px"><h4>Birth</h4><p class="small">This gives information about the pregnancy &amp;<br>birth. Lorem ipsum dolor sit amet, consectetur<br>adipiscing elit, sed do eiusmod tempor</p></div>
  <div class="abs stage-icon" style="left:476px;top:1734px"></div>

  <div class="abs ribbon">Pregnancy Stages</div>
  <div class="abs stages-art" role="img" aria-label="Illustration of four pregnant silhouettes showing each stage of pregnancy"></div>
  <div class="abs timeline">
    <span style="background:#9c5aa8">I Trimester</span>
    <span style="background:#b15fa6">II Trimester</span>
    <span style="background:#8a4a9c">III Trimester</span>
    <span style="background:#d05aa4">Birth</span>
  </div>

  <!-- latest posts -->
  <h2 class="abs heading section-title" style="top:1914px">Latest Posts</h2>
  <p class="abs section-sub" style="top:1944px">Latest articles published by Lorvin Medical</p>
  <div class="abs rule" style="top:1964px"></div>

  <article class="abs post" style="left:258px;top:1992px">
    <div class="post-photo" role="img" aria-label="Photo of a parent holding a baby's hand"></div>
    <div class="post-date">FEB<br>12</div>
    <h4>10 Simple Baby Care Tricks Mom Never Told You</h4>
    <p class="small">Your mom has been there through the ups and downs, the heartaches and the good times, but she doesn't know everything</p>
    <span class="read-more">Read More</span>
  </article>
  <article class="abs post" style="left:462px;top:1992px">
    <div class="post-photo" role="img" aria-label="Photo of parents with their newborn in hospital"></div>
    <div class="post-date">FEB<br>12</div>
    <h4>Parents Say: How to Care for a Newborn Baby</h4>
    <p class="small">The first few weeks with your newborn will be chaotic. Here are a few tips from experienced parents to help make</p>
    <span class="read-more">Read More</span>
  </article>
  <article class="abs post" style="left:666px;top:1992px">
    <div class="post-photo" role="img" aria-label="Photo of a newborn baby resting"></div>
    <div class="post-date">FEB<br>12</div>
    <h4>Parenting Care-Bonding With Your Newborn</h4>
    <p class="small">When experts talk about bonding, they're referring to the intense attachment you develop with your baby.</p>
    <span class="read-more">Read More</span>
  </article>

  <!-- footer -->
  <footer class="abs footer" role="img" aria-label="Dark photo backdrop of a nursery"></footer>
  <div class="abs foot-col" style="left:254px;top:2336px"><h5>About Lorvin Medical</h5><ul><li><b></b>Contact Us</li><li><b></b>(02) 55 010 240</li><li><b></b>www.lorvinmedical.com</li><li><b></b>14 Alder Lane 4410 2090</li></ul></div>
  <div class="abs foot-col" style="left:424px;top:2336px"><h5>Navigation</h5><ul><li><b></b>Fertility</li><li><b></b>Pregnancy Basics</li><li><b></b>Articles</li><li><b></b>Tips &amp; News</li><li><b></b>Contact Us</li></ul></div>
  <div class="abs foot-col" style="left:562px;top:2336px"><h5>Extra Navigation</h5><ul><li><b></b>Getting Pregnant</li><li><b></b>Your First Scan</li><li><b></b>Pregnant</li><li><b></b>Baby Birth</li><li><b></b>Feeding Baby</li></ul></div>
  <div class="abs foot-photo" role="img" aria-label="Photo of a baby's tiny feet held in hands"></div>

  <section class="abs subscribe"></section>
  <div class="abs" style="left:254px;top:2528px"><h5 class="heading" style="font-size:12px;color:#fff">Subscribe to us!</h5><p style="font-size:8px;color:#f3f8dc">Subscribe to our monthly newsletter</p></div>
  <div class="abs sub-field"></div>
  <div class="abs sub-go"></div>
  <div class="abs social" style="left:718px"></div>
  <div class="abs social" style="left:752px"></div>
  <div class="abs social" style="left:786px"></div>
  <div class="abs social" style="left:820px"></div>
  <div class="abs social" style="left:854px"></div>

  <div class="abs copyright">© Copyright <span style="color:var(--green)">Lorvin Medical</span> 2017. All Rights Reserved</div>
</main>
</body>
</html>
```